Multi brand diverse distributor requires new business card

We're a distributor representing multiple brands and would like a new business card reflecting our diversity.

We incorporate landscape architecture, environmental engineering and sustainability into construction projects.

KV Group is the company name, and therefore the KV logo should be the primary logo.

Target Market(s)

Engineers, Landscape Architects, Environmental

Contact Information for Business Card

See sample

Colors

Designer to choose colors to be used in the design.

```html
<!DOCTYPE html>
<html lang="en">
<head>
<meta charset="utf-8">
<title>KV Group – Business Card</title>
<link rel="stylesheet" href="https://fonts.googleapis.com/css2?family=Exo+2:wght@400;500;600;700;800&display=swap">
<style>
  :root{
    --bg:#e4e4e4;
    --crimson:#c2103f;
    --crimson-deep:#b5093a;
    --white:#ffffff;
    --ink:#111111;
    --card-dark:#1c1d1f;
    --silver:#d8d8d8;
    --steel:#8a8b8d;
    --muted:#9a9a9a;
  }
  *{margin:0;padding:0;box-sizing:border-box}
  html,body{width:1200px;height:1200px;overflow:hidden;background:var(--bg);font-family:"Exo 2",sans-serif}
  .sheet{position:relative;width:1200px;height:1200px}
  .card{position:absolute;left:190px;width:820px;height:468px;border-radius:26px;overflow:hidden}
  .card-front{top:100px;background:linear-gradient(180deg,var(--crimson),var(--crimson-deep))}
  .card-back{top:632px;background:var(--card-dark)}
  .card-shape{position:absolute;inset:0;width:100%;height:100%}

  .person{position:absolute;left:55px;top:155px;color:var(--white)}
  .person-name{font-size:29px;font-weight:700;letter-spacing:0.5px;line-height:1}
  .person-title{font-size:16px;font-weight:600;margin-top:8px}
  .contacts{position:absolute;left:55px;top:236px;list-style:none;color:var(--white)}
  .contacts li{display:flex;align-items:center;font-size:19px;font-weight:400;height:23.5px}
  .contacts svg{width:14px;height:14px;margin-right:12px;flex:none}

  .brand-front{position:absolute;left:482px;top:158px;width:210px;text-align:center;color:var(--crimson)}
  .brand-front .mark{font-size:118px;font-weight:800;line-height:1;letter-spacing:-4px}
  .brand-front .word{font-size:21px;font-weight:800;letter-spacing:22px;margin-left:22px;margin-top:-2px}
  .brand-front .rule{height:3px;background:var(--crimson);margin-top:6px}
  .brand-front .est{color:var(--ink);font-size:17px;font-weight:600;letter-spacing:4px;margin-top:9px}

  .brand-back{position:absolute;left:189px;top:136px;width:442px;color:var(--silver)}
  .brand-back .mark{position:absolute;left:0;top:0;font-size:118px;font-weight:800;line-height:1;letter-spacing:-4px}
  .brand-back .word{position:absolute;left:214px;top:54px;font-size:50px;font-weight:800;letter-spacing:4px;line-height:1}
  .brand-back .est{position:absolute;left:262px;top:10px;color:var(--steel);font-size:19px;font-weight:600;letter-spacing:7px}
  .brand-back .rule{position:absolute;left:0;top:121px;width:442px;height:2px;background:var(--silver)}
  .cities{position:absolute;left:0;right:0;top:268px;text-align:center;color:var(--white);font-size:20px;font-weight:500}
  .cities .dot{display:inline-block;width:10px;height:10px;border-radius:50%;background:var(--crimson);margin:0 4px 1px}

  .partners{position:absolute;left:0;right:0;top:380px;height:40px}
  .partner{position:absolute;top:0;height:40px;display:flex;align-items:center;justify-content:center;gap:8px;color:var(--muted);font-size:19px;font-weight:600;transform:translateX(-50%);white-space:nowrap}
  .partner .chip{width:16px;height:16px;background:var(--steel)}
  .partner .chip.round{border-radius:50%}
</style>
</head>
<body>
<main class="sheet">

  <section class="card card-front">
    <svg class="card-shape" viewBox="0 0 800 457" preserveAspectRatio="none" aria-hidden="true">
      <path d="M633,457 Q800,457 800,290 V457 Z" fill="var(--ink)"/>
      <path d="M352,457 V180 Q352,0 527,0 H800 V290 Q800,457 633,457 Z" fill="var(--white)"/>
    </svg>

    <div class="person">
      <h1 class="person-name">MARCO BELLANDI</h1>
      <p class="person-title">B.Eng (Civil)</p>
    </div>

    <ul class="contacts">
      <li><svg viewBox="0 0 16 16"><path fill="#fff" d="M3.6 1.5l2.3 2.6-1.3 1.9c.8 1.9 2.4 3.5 4.3 4.4l1.9-1.3 2.6 2.3-1.2 2.3C7.4 14.3 1.7 8.6 1.3 3z"/></svg>0400 218 735</li>
      <li><svg viewBox="0 0 16 16"><rect x="4" y="1" width="8" height="14" rx="1.5" fill="none" stroke="#fff" stroke-width="1.8"/><rect x="7" y="12" width="2" height="1.4" fill="#fff"/></svg>1300 472 915</li>
      <li><svg viewBox="0 0 16 16"><rect x="1" y="4" width="14" height="9" fill="#fff"/><path d="M1.5 4.5L8 9.5l6.5-5" fill="none" stroke="var(--crimson)" stroke-width="1.3"/></svg>marco@kvgroup.com.au</li>
      <li><svg viewBox="0 0 16 16"><circle cx="8" cy="8" r="7" fill="#fff"/><path d="M4 4.5c2 .5 2.5 2 1.5 3.5S7 10.5 7 13M10 3c-.5 1.5.5 2.5 2 3s1 3 0 4" fill="none" stroke="var(--crimson)" stroke-width="1.4"/></svg>www.kvgroup.com.au</li>
    </ul>

    <div class="brand-front">
      <div class="mark">KV</div>
      <div class="word">GROUP</div>
      <div class="rule"></div>
      <div class="est">EST. 1971</div>
    </div>
  </section>

  <section class="card card-back">
    <div class="brand-back">
      <div class="mark">KV</div>
      <div class="est">EST. 1971</div>
      <div class="word">GROUP</div>
      <div class="rule"></div>
    </div>

    <p class="cities">Adelaide<span class="dot"></span>Brisbane<span class="dot"></span>Melbourne<span class="dot"></span>Perth<span class="dot"></span>Sydney</p>

    <div class="partners">
      <div class="partner" style="left:140px"><span class="chip"></span>Lumen Deck</div>
      <div class="partner" style="left:311px"><span class="chip round"></span>AquaWise</div>
      <div class="partner" style="left:481px"><span class="chip"></span>Corvex</div>
      <div class="partner" style="left:657px"><span class="chip round" style="background:var(--crimson)"></span>Urban Seat Co</div>
    </div>
  </section>

</main>
</body>
</html>
```